QZN Supplements needs a label designer for supplement company

Looking for an on going label designer for my supplement company. I have three products that will need designs. I'm about to launch my sleep supplement called Velmora Rest and that's the first design needed.
I would like all designs to be somewhat simple, not overstated and uniformed so that when you look at all of the labels of the different supplements they are similar and you can tell it's the same brand.
Please see attached sample pictures below as ideas.
Updates

The brand is QZN supplements, logo file has been provided. The supplement is called Velmora Rest. It is a liquid supplement that is a 32/33 ounce white bottle. Die lines and measurements will be provided. Here's text for wording ideas: Wording: Natural Sleep Aid Reset your circadian rhythm. May help you: Fall asleep faster. Get a deeper more restful sleep. Boost Immune System Remember your dreams. Protect your brain and flush toxins. Wake up feeling refreshed. Non-gmo Gluten Free Sugar Free Vegan Manufactured in cGMP factory Manufactured in USA

Target Market(s)

Health and wellness/supplement industry for regular people not hardcore gym goers. My supplements are for a health lifestyle not bodybuilding.

Industry/Entity Type

Health And Wellness

Colors
3176b5
3276b5
33a6d7
85cae6
85abd2
cedeed
e4daeb
b7a5cd

Requirements
Must have
• There will be some text and wording that I will provide that must be on the bottles.

```html
<!DOCTYPE html>
<html lang="en">
<head>
<meta charset="utf-8">
<title>Velmora Rest — Label</title>
<link rel="stylesheet" href="https://fonts.googleapis.com/css2?family=Oswald:wght@400&family=Roboto:wght@400;700&display=swap">
<style>
  :root {
    --page: #ffffff;
    --label: #7a86bf;
    --swoosh-deep: #6a6fb8;
    --band: #20225e;
    --ink: #ffffff;
    --mark: #e9a85c;
  }
  * { box-sizing: border-box; margin: 0; padding: 0; }
  html, body {
    width: 1200px;
    height: 1002px;
    overflow: hidden;
    background: var(--page);
  }
  .canvas {
    position: relative;
    width: 1200px;
    height: 1002px;
  }
  .label {
    position: absolute;
    left: 395px;
    top: 31px;
    width: 410px;
    height: 940px;
    overflow: hidden;
    background: var(--label);
    color: var(--ink);
    font-family: "Roboto", Arial, sans-serif;
    text-align: center;
  }
  .swoosh-area {
    position: absolute;
    left: -40px;
    top: 60px;
    width: 190px;
    height: 560px;
    border-radius: 0 100% 0 60%;
    background: linear-gradient(160deg, var(--swoosh-deep) 0%, rgba(106, 111, 184, 0.35) 70%, rgba(106, 111, 184, 0) 100%);
  }
  .brand-mark {
    position: absolute;
    top: 30px;
    right: 22px;
    display: flex;
    align-items: center;
    gap: 8px;
    font-size: 17px;
    font-weight: 400;
    color: var(--mark);
  }
  .brand-mark .dot {
    width: 14px;
    height: 14px;
    border-radius: 50%;
    border: 2px solid var(--mark);
  }
  .product-name {
    position: absolute;
    top: 200px;
    left: 0;
    width: 100%;
    font-family: "Oswald", "Arial Narrow", sans-serif;
    font-weight: 400;
    font-size: 90px;
    line-height: 96px;
    letter-spacing: 1px;
  }
  .moon-icon {
    position: absolute;
    top: 420px;
    left: 168px;
    width: 74px;
    height: 80px;
  }
  .benefits {
    position: absolute;
    top: 520px;
    left: 0;
    width: 100%;
    list-style: none;
    font-size: 24px;
    line-height: 40px;
    text-transform: uppercase;
  }
  .claims-band {
    position: absolute;
    top: 657px;
    left: 0;
    width: 100%;
    height: 114px;
    background: var(--band);
    padding-top: 16px;
    font-size: 27px;
    line-height: 40px;
    text-transform: uppercase;
  }
  .net-volume {
    position: absolute;
    top: 802px;
    left: 0;
    width: 100%;
    font-size: 19px;
    font-weight: 700;
  }
  .supplement-type {
    position: absolute;
    top: 856px;
    left: 0;
    width: 100%;
    font-size: 19px;
    font-weight: 700;
    letter-spacing: 3px;
    text-transform: uppercase;
  }
</style>
</head>
<body>
<main class="canvas">
  <section class="label">
    <div class="swoosh-area" role="img" aria-label="Soft decorative swoosh shape in deep violet"></div>

    <div class="brand-mark"><span class="dot"></span>QZN Supplements</div>

    <h1 class="product-name">VELMORA<br>REST</h1>

    <svg class="moon-icon" viewBox="0 0 74 80" aria-hidden="true">
      <path d="M30 24 A26 26 0 1 0 56 62 A22 22 0 0 1 30 24 Z" fill="none" stroke="var(--ink)" stroke-width="3"/>
      <text x="48" y="22" fill="var(--ink)" font-family="Roboto, sans-serif" font-size="16">z</text>
      <text x="56" y="32" fill="var(--ink)" font-family="Roboto, sans-serif" font-size="14">z</text>
      <text x="62" y="42" fill="var(--ink)" font-family="Roboto, sans-serif" font-size="12">z</text>
    </svg>

    <ul class="benefits">
      <li>Natural Sleep Aid</li>
      <li>Reset Your Circadian Rhythm</li>
      <li>Boost Immune System</li>
    </ul>

    <div class="claims-band">
      <p>Non-GMO | Gluten Free</p>
      <p>Sugar Free | Vegan</p>
    </div>

    <p class="net-volume">32 oz</p>
    <p class="supplement-type">Dietary Supplement</p>
  </section>
</main>
</body>
</html>
```